Marvel Brookworks highend custom homes

We build high end custom homes and timber frames we specialize in rustic hand made designs along with iron and concrete accents to add a modern touch 90% of my homes are buit on lake front properries attached is my logo and slogan as of now and my previous one

Target Market(s)

High end custom homes

Industry/Entity Type

Custom residential construction

Contact Information for Business Card

Been in buissness 8+ years inssured and reliable

Colors
A7469A
B969AE
D3A5CF
EDDBEB
F8F0F9

Requirements
Must have
• Must have slogan and phone number
Should not have
• A combination of rustic yet modern accents

```html
<!DOCTYPE html>
<html lang="en">
<head>
<meta charset="utf-8">
<title>Marvel Brookworks – Business Card</title>
<link rel="stylesheet" href="https://fonts.googleapis.com/css2?family=Montserrat:wght@300;400;700&display=swap">
<style>
  :root {
    --plum: #A7469A;
    --orchid: #B969AE;
    --lilac: #D3A5CF;
    --blush: #EDDBEB;
    --mist: #F8F0F9;
    --ink-grey: #8a8a8e;
    --stage: #e6e4e8;
    --paper: #ffffff;
  }
  * { box-sizing: border-box; margin: 0; padding: 0; }
  html, body {
    width: 1200px; height: 1200px; overflow: hidden;
    background: var(--stage);
    font-family: "Montserrat", sans-serif;
  }
  .canvas { position: relative; width: 1200px; height: 1200px; }
  .card {
    position: absolute; left: 220px; width: 760px; height: 434px;
    box-shadow: 0 10px 30px rgba(0,0,0,0.18);
  }
  .brand-name {
    display: flex; align-items: center; font-weight: 700;
    text-transform: uppercase; white-space: nowrap;
  }
  .slogan { font-weight: 400; text-transform: uppercase; white-space: nowrap; }

  /* Back side */
  .card--back {
    top: 120px;
    background: radial-gradient(ellipse at 30% 80%, var(--orchid) 0%, var(--plum) 85%);
    display: flex; align-items: center; justify-content: center;
  }
  .back-brand { text-align: center; color: var(--lilac); opacity: 0.75; }
  .back-brand .brand-name { gap: 16px; font-size: 38px; letter-spacing: 2px; }
  .back-brand .brand-mark { width: 26px; height: 26px; background: var(--lilac); flex: none; }
  .back-brand .slogan { margin-top: 12px; font-size: 15px; letter-spacing: 3px; }

  /* Front side */
  .card--front {
    top: 646px;
    background: linear-gradient(160deg, var(--paper) 0%, #f4f4f5 100%);
  }
  .holder {
    position: absolute; left: 52px; top: 48px;
    display: flex; align-items: baseline; gap: 10px;
  }
  .holder-name { color: var(--plum); font-weight: 700; font-size: 30px; }
  .holder-divider { width: 1.5px; height: 28px; background: var(--lilac); align-self: center; }
  .holder-role { color: var(--ink-grey); font-weight: 300; font-size: 22px; letter-spacing: 0.5px; }

  .contacts {
    position: absolute; left: 52px; top: 180px;
    list-style: none; color: var(--ink-grey); font-size: 19px; font-weight: 400;
  }
  .contacts li { display: flex; align-items: center; gap: 12px; line-height: 34px; }
  .contacts svg { width: 18px; height: 18px; fill: var(--plum); flex: none; }

  .front-brand { position: absolute; right: 48px; bottom: 40px; color: var(--plum); }
  .front-brand .brand-name { gap: 12px; font-size: 26px; letter-spacing: 1.5px; }
  .front-brand .brand-mark { width: 20px; height: 20px; background: var(--plum); flex: none; }
  .front-brand .slogan { margin-top: 8px; padding-left: 32px; font-size: 12.5px; letter-spacing: 2.5px; }
</style>
</head>
<body>
<main class="canvas">
  <section class="card card--back">
    <div class="back-brand">
      <div class="brand-name"><span class="brand-mark"></span>Marvel Brookworks</div>
      <div class="slogan">Lakefront homes, built by hand</div>
    </div>
  </section>

  <section class="card card--front">
    <div class="holder">
      <span class="holder-name">Dalia Fenwick</span>
      <span class="holder-divider"></span>
      <span class="holder-role">Founder &amp; Director</span>
    </div>

    <ul class="contacts">
      <li>
        <svg viewBox="0 0 24 24" aria-hidden="true"><path d="M6.6 10.8a15.1 15.1 0 0 0 6.6 6.6l2.2-2.2a1 1 0 0 1 1-.25 11.4 11.4 0 0 0 3.6.57 1 1 0 0 1 1 1V20a1 1 0 0 1-1 1A17 17 0 0 1 3 4a1 1 0 0 1 1-1h3.5a1 1 0 0 1 1 1c0 1.25.2 2.45.57 3.6a1 1 0 0 1-.25 1z"/></svg>
        +1 (555) 014 2276
      </li>
      <li>
        <svg viewBox="0 0 24 24" aria-hidden="true"><path d="M2 5h20v2l-10 6.5L2 7z"/><path d="M2 9l10 6.5L22 9v10H2z"/></svg>
        hello@marvelbrookworks.com
      </li>
      <li>
        <svg viewBox="0 0 24 24" aria-hidden="true"><path d="M12 2a10 10 0 1 0 0 20 10 10 0 0 0 0-20zm6.9 6h-3a15.6 15.6 0 0 0-1.3-3.9A8 8 0 0 1 18.9 8zM12 4c.8 1.1 1.5 2.5 1.9 4h-3.8c.4-1.5 1.1-2.9 1.9-4zM4.3 14a8 8 0 0 1 0-4h3.4a16.5 16.5 0 0 0 0 4zm.8 2h3a15.6 15.6 0 0 0 1.3 3.9A8 8 0 0 1 5.1 16zm3-8h-3a8 8 0 0 1 4.3-3.9A15.6 15.6 0 0 0 8.1 8zM12 20c-.8-1.1-1.5-2.5-1.9-4h3.8c-.4 1.5-1.1 2.9-1.9 4zm2.3-6H9.7a14.7 14.7 0 0 1 0-4h4.6a14.7 14.7 0 0 1 0 4zm.3 5.9a15.6 15.6 0 0 0 1.3-3.9h3a8 8 0 0 1-4.3 3.9zm1.7-5.9a16.5 16.5 0 0 0 0-4h3.4a8 8 0 0 1 0 4z"/></svg>
        www.marvelbrookworks.com
      </li>
    </ul>

    <div class="front-brand">
      <div class="brand-name"><span class="brand-mark"></span>Marvel Brookworks</div>
      <div class="slogan">Lakefront homes, built by hand</div>
    </div>
  </section>
</main>
</body>
</html>
```